Stationary Design needed for luxorious bespoke tailor

We need a design for our stationary items like businescards, letters, envelope and letter head / Signature for email. Our company "VELMARDO" sells exclusively and luxourious bespoke garments and accessories for men. The desgins of letterhead, envelope and business card shoulderstand communicate luxury, high quality and good taste. We would like our logo to be used on the designs.

Target Market(s)

Gentleman with a high aproach and exclusive and luxourious suits and shirts, grooms, businesman,

Industry/Entity Type

It Company

Font styles to use
Sans Serif

Colors
ec1f27
ffffff

Requirements
Must have
• Logo, Companies name and adress, contactName internet & email, phone number line / mobile, VAT Nr. On Business Card frontpage only logo and name, adress companies on backpage. No VAT and Companies ID there. Company data; VELMARDO AG Sonnwiesweg 27 4068 Basel Switzerland VAT: CHE 472 916 503 Tax Tel 41 61 508 37 14 Mobile 41 79 842 07 91 www.velmardo.ch info@velmardo.com.
Nice to have
• -Name And phone numbers need to be able to change (for different coworkers ...)
Should not have
• no VAT in Business Card

```html
<!DOCTYPE html>
<html lang="en">
<head>
<meta charset="utf-8">
<title>VELMARDO Stationery</title>
<link rel="stylesheet" href="https://fonts.googleapis.com/css2?family=Open+Sans:wght@400;600&display=swap">
<style>
:root{
  --bg:#2c2c2c;
  --paper:#ffffff;
  --ink:#0b0b0b;
  --red:#ec1f27;
  --grey:#555555;
}
*{margin:0;padding:0;box-sizing:border-box}
html,body{width:1200px;height:779px;overflow:hidden;background:var(--bg);font-family:"Open Sans",sans-serif;color:var(--grey)}
.canvas{position:relative;width:1200px;height:779px}
.sheet{position:absolute;background:var(--paper);box-shadow:0 2px 6px rgba(0,0,0,.45)}
.band{position:absolute;left:0;right:0;bottom:0;display:flex}
.band .black{background:var(--ink)}
.band .red{background:var(--red);flex:1}
.wordmark{position:absolute;left:0;right:0;text-align:center;font-weight:600;color:var(--ink);letter-spacing:.08em;line-height:1}
.wordmark.light{color:var(--paper)}
.red-label{color:var(--red)}
address{font-style:normal}

/* letterhead */
.letterhead{left:47px;top:32px;width:501px;height:706px}
.letterhead .wordmark{top:38px;font-size:22px}
.letterhead .address{position:absolute;left:20px;top:629px;font-size:9.5px;line-height:13px}
.letterhead .contact{position:absolute;right:20px;top:629px;font-size:9.5px;line-height:13px;text-align:right}
.letterhead .band{height:8px}
.letterhead .band .black{width:249px}

/* business cards */
.card-front{left:595px;top:34px;width:248px;height:142px}
.card-front .wordmark{top:55px;font-size:20px}
.card-front .person{position:absolute;left:0;right:0;top:103px;text-align:center}
.person .name{font-size:9.5px;font-weight:600;color:var(--red);line-height:12px}
.person .role{font-size:7px;color:var(--ink);line-height:10px}

.card-back{left:872px;top:34px;width:248px;height:142px}
.card-back .details{position:absolute;left:0;right:0;top:52px;text-align:center;font-size:6px;line-height:8.5px}
.card-back .details .gap{height:6px}
.card-back .band{height:6px}
.card-back .band .black{width:123px}

.card-wide{left:701px;top:210px;width:330px;height:146px}
.card-wide .top{position:absolute;left:0;top:0;right:0;height:80px;background:var(--ink)}
.card-wide .wordmark{top:15px;font-size:18px}
.card-wide .person{position:absolute;left:0;right:0;top:48px;text-align:center}
.card-wide .person .name{font-size:10px}
.card-wide .person .role{color:var(--paper)}
.card-wide .details{position:absolute;left:0;right:0;top:98px;text-align:center;font-size:6.8px;line-height:12px}
.card-wide .band{height:6px}
.card-wide .band .black{width:165px}

/* envelope */
.envelope-back{position:absolute;left:643px;top:379px;width:509px;height:227px}
.envelope-back svg{position:absolute;inset:0}
.envelope-back .wordmark{top:36px;font-size:14px}
.envelope-front{left:582px;top:505px;width:514px;height:230px}
.envelope-front .sender{position:absolute;left:26px;top:29px;font-size:8.5px;line-height:12.3px}
.envelope-front .band{height:8px}
.envelope-front .band .black{width:258px}
</style>
</head>
<body>
<main class="canvas">

  <section class="sheet letterhead">
    <div class="wordmark">VELMARDO</div>
    <address class="address">VELMARDO AG<br>Sonnwiesweg 27<br>4068 Basel<br>Switzerland</address>
    <div class="contact">
      CHE-472.916.503 MwSt<br>
      <span class="red-label">P</span> : +41 61 508 37 14<br>
      <span class="red-label">E</span> : info@velmardo.com<br>
      <span class="red-label">W</span> : www.velmardo.ch
    </div>
    <div class="band"><span class="black"></span><span class="red"></span></div>
  </section>

  <section class="sheet card-front">
    <div class="wordmark">VELMARDO</div>
    <div class="person"><div class="name">ANDREAS KELLER</div><div class="role">CEO/Founder</div></div>
  </section>

  <section class="sheet card-back">
    <div class="details">
      VELMARDO AG, Sonnwiesweg 27<br>4068 Basel , Switzerland
      <div class="gap"></div>
      <span class="red-label">P</span> : +41 61 508 37 14 &nbsp;<span class="red-label">M</span> : +41 79 842 07 91<br>
      <span class="red-label">E</span> : info@velmardo.com &nbsp; <span class="red-label">W</span> : www.velmardo.ch
    </div>
    <div class="band"><span class="black"></span><span class="red"></span></div>
  </section>

  <section class="sheet card-wide">
    <div class="top"></div>
    <div class="wordmark light">VELMARDO</div>
    <div class="person"><div class="name">ANDREAS KELLER</div><div class="role">CEO/Founder</div></div>
    <div class="details">
      VELMARDO AG, Sonnwiesweg 27, 4068 Basel , Switzerland<br>
      <span class="red-label">P</span> : +41 61 508 37 14 &nbsp;<span class="red-label">M</span> : +41 79 842 07 91 <span class="red-label">E</span> : info@velmardo.com <span class="red-label">W</span> : velmardo.ch
    </div>
    <div class="band"><span class="black"></span><span class="red"></span></div>
  </section>

  <section class="envelope-back">
    <svg width="509" height="227" viewBox="0 0 509 227">
      <rect x="0" y="0" width="509" height="227" fill="#ffffff"/>
      <path d="M130 227 L180 110 H330 L380 227" fill="none" stroke="#e6e6e6" stroke-width="1.5"/>
      <path d="M440 160 L504 227" fill="none" stroke="#e6e6e6" stroke-width="1.5"/>
      <path d="M0 0 H509 L497 60 Q492 85 465 85 H44 Q17 85 12 60 Z" fill="#0b0b0b"/>
    </svg>
    <div class="wordmark light">VELMARDO</div>
  </section>

  <section class="sheet envelope-front">
    <address class="sender">VELMARDO AG<br>Sonnwiesweg 27<br>4068 Basel, Switzerland</address>
    <div class="band"><span class="black"></span><span class="red"></span></div>
  </section>

</main>
</body>
</html>
```